Business price tag design for Furniture Business

Hello,

I have developed a tag for a home furniture business and need 1 more creative template. Please see attachment. I need the template to be very appealing.

Requirements:

1.Tag dimensions needs to be about the same as attached tag.
2. Tag design needs to be suitable for a home furniture business.
3. Tag needs to have locations for the following: Item Title, Now Price, Was Price, Product Number.
4. "The black shape at the bottom of attached tag could be removed.

I have no requirements on colors, but something professional is needed, preferably white background to reduce print ink consumption.

Please see attachment for clarification.

Industry/Entity Type

Retail

Font styles to use
Serif
Sans Serif

Requirements
Must have
• Please see Project Description.
Nice to have

```html
<!DOCTYPE html>
<html lang="en">
<head>
<meta charset="UTF-8">
<title>Furniture Price Tag</title>
<link href="https://fonts.googleapis.com/css2?family=Libre+Baskerville:wght@400;700&family=Arimo:wght@700&display=swap" rel="stylesheet">
<style>
  :root {
    --page: #ffffff;
    --paper: #ffffff;
    --leather-black: #1f201e;
    --leather-black-light: #3a3b38;
    --leather-red: #8e2a26;
    --leather-red-dark: #6a1b18;
    --burgundy: #8a2a25;
    --ink: #111111;
    --cream: #f2e3bd;
    --cream-dark: #e3cf9c;
    --stitch-light: #b9b7ad;
    --stitch-red: #d98b7e;
    --white: #ffffff;
  }
  * { margin: 0; padding: 0; box-sizing: border-box; }
  html, body {
    width: 793px;
    height: 1200px;
    overflow: hidden;
    background: var(--page);
  }
  .canvas {
    position: relative;
    width: 793px;
    height: 1200px;
  }
  .tag {
    position: absolute;
    left: 212px;
    top: 244px;
    width: 408px;
    height: 816px;
    background: var(--paper);
  }
  .band {
    position: absolute;
    left: 0;
    width: 100%;
  }
  .band svg { display: block; width: 100%; height: 100%; }
  .band--top { top: 0; height: 101px; box-shadow: 0 8px 10px -4px rgba(0,0,0,0.35); }
  .band--sale { top: 434px; height: 212px; box-shadow: 0 -6px 10px -4px rgba(0,0,0,0.35); }
  .band--delivery { top: 644px; height: 172px; }

  .item-title {
    position: absolute;
    left: 0;
    width: 100%;
    top: 120px;
    text-align: center;
    font-family: "Libre Baskerville", "Times New Roman", serif;
    font-weight: 700;
    font-size: 50px;
    color: var(--burgundy);
    letter-spacing: 0.5px;
  }
  .product-number {
    position: absolute;
    left: 14px;
    top: 196px;
    font-family: "Arimo", Arial, sans-serif;
    font-weight: 700;
    font-size: 20px;
    color: var(--ink);
  }
  .was-label {
    position: absolute;
    left: 14px;
    top: 300px;
    font-family: "Arimo", Arial, sans-serif;
    font-weight: 700;
    font-size: 34px;
    color: var(--burgundy);
  }
  .was-price {
    position: absolute;
    right: 38px;
    top: 352px;
    font-family: "Arimo", Arial, sans-serif;
    font-weight: 700;
    font-size: 34px;
    color: var(--burgundy);
  }
  .now-label {
    position: absolute;
    left: 12px;
    top: 488px;
    font-family: "Arimo", Arial, sans-serif;
    font-weight: 700;
    font-size: 54px;
    color: var(--white);
  }
  .now-price {
    position: absolute;
    left: 190px;
    top: 477px;
    width: 202px;
    height: 106px;
    border-radius: 12px;
    background: linear-gradient(160deg, var(--cream) 0%, #f7ecd0 50%, var(--cream-dark) 100%);
    box-shadow: 0 3px 8px rgba(0,0,0,0.45);
    display: flex;
    align-items: center;
    justify-content: center;
    font-family: "Arimo", Arial, sans-serif;
    font-weight: 700;
    font-size: 42px;
    color: var(--ink);
  }
  .delivery-note {
    position: absolute;
    left: 0;
    width: 100%;
    top: 690px;
    text-align: center;
    font-family: "Arimo", Arial, sans-serif;
    font-weight: 700;
    font-size: 38px;
    line-height: 58px;
    color: var(--white);
  }
</style>
</head>
<body>
<div class="canvas">
  <div class="tag">
    <div class="band band--top">
      <svg viewBox="0 0 408 101" preserveAspectRatio="none" role="img" aria-label="Black leather strip">
        <defs>
          <linearGradient id="blackLeatherTop" x1="0" y1="0" x2="0" y2="1">
            <stop offset="0" stop-color="var(--leather-black-light)"/>
            <stop offset="1" stop-color="var(--leather-black)"/>
          </linearGradient>
        </defs>
        <rect width="408" height="101" fill="url(#blackLeatherTop)"/>
        <line x1="0" y1="84" x2="408" y2="84" stroke="var(--stitch-light)" stroke-width="2" stroke-dasharray="9 5"/>
      </svg>
    </div>

    <h1 class="item-title">ITEM TITLE</h1>
    <p class="product-number">PRODUCT #</p>
    <p class="was-label">WAS:</p>
    <p class="was-price">$000.00</p>

    <div class="band band--sale">
      <svg viewBox="0 0 408 212" preserveAspectRatio="none" role="img" aria-label="Red leather strip">
        <defs>
          <linearGradient id="redLeather" x1="0" y1="0" x2="0" y2="1">
            <stop offset="0" stop-color="var(--leather-red)"/>
            <stop offset="1" stop-color="var(--leather-red-dark)"/>
          </linearGradient>
        </defs>
        <rect width="408" height="212" fill="url(#redLeather)"/>
        <line x1="0" y1="16" x2="408" y2="16" stroke="var(--stitch-red)" stroke-width="2" stroke-dasharray="9 5"/>
        <line x1="0" y1="194" x2="408" y2="194" stroke="var(--stitch-red)" stroke-width="2" stroke-dasharray="9 5"/>
      </svg>
    </div>
    <p class="now-label">NOW</p>
    <div class="now-price">$000.00</div>

    <div class="band band--delivery">
      <svg viewBox="0 0 408 172" preserveAspectRatio="none" role="img" aria-label="Black leather strip">
        <defs>
          <linearGradient id="blackLeatherBottom" x1="0" y1="0" x2="0" y2="1">
            <stop offset="0" stop-color="var(--leather-black)"/>
            <stop offset="0.5" stop-color="var(--leather-black-light)"/>
            <stop offset="1" stop-color="var(--leather-black)"/>
          </linearGradient>
        </defs>
        <rect width="408" height="172" fill="url(#blackLeatherBottom)"/>
        <line x1="0" y1="18" x2="408" y2="18" stroke="var(--stitch-light)" stroke-width="2" stroke-dasharray="9 5"/>
      </svg>
    </div>
    <p class="delivery-note">NEED DELIVERY?<br>NO PROBLEM!</p>
  </div>
</div>
</body>
</html>
```